Personal Brand (Influencer) Website

I'm looking for a brand new website design for a youtuber/influencer Dane Whitaker.

I'm looking for a sleek design that is visually appealing while still maintaining full functionality and user experience.

Here is our current website: http://danewhitakerhq.example/

I want to combine some of the best elements and designs from the following websites.

https://www.milofenwright.example/
https://www.renzovale.example/
https://quinnbarlow.example/
https://www.silasmerrow.example/
http://danewhitakerhq.example/
http://www.kenfrayle.example/

Here are the different tabs that I would need designed as well as the main page:

Home Page (main page)
Blogs
My story (about me)
Top 100 book list
Contact

Here are several links and social media handles for you to get a better gauge on the branding of Dane Whitaker:
https://www.videohub.example/channel/XQpar3k9v-T2mhZZ_QWrta7z
https://trend-rocket.example/market-blog/uncategorized/dane-whitaker-entrepreneur-winning-market-follow-data-ep-17/
https://danelisten2.pagepath.example/optin-48203917
https://www.snapgrid.example/officialdanewhitaker/

```html
<!DOCTYPE html>
<html lang="en">
<head>
<meta charset="utf-8">
<title>Dane Whitaker — Live Life on Your Terms</title>
<link rel="stylesheet" href="https://fonts.googleapis.com/css2?family=Montserrat:wght@400;500;600;700;800&family=Yellowtail&display=swap">
<style>
  :root {
    --blue: #1a8ae6;
    --ink: #1f2230;
    --muted: #7b7f8c;
    --price: #e0383e;
    --white: #ffffff;
    --card: #f3f4f6;
    --line: #d8dbe2;
    --hero-top: #b3a9bd;
    --hero-bottom: #4f4560;
  }
  * { box-sizing: border-box; margin: 0; padding: 0; }
  html, body { width: 675px; height: 1200px; overflow: hidden; }
  body { font-family: "Montserrat", sans-serif; color: var(--ink); background: var(--white); }
  .page { width: 675px; height: 1200px; position: relative; overflow: hidden; }

  /* Hero */
  .hero { position: relative; height: 250px; color: var(--white); text-align: center; overflow: hidden; }
  .hero-photo { position: absolute; inset: 0; background: linear-gradient(180deg, var(--hero-top) 0%, #7d7190 55%, var(--hero-bottom) 100%); }
  .topbar { position: absolute; top: 14px; left: 48px; right: 48px; display: flex; align-items: center; justify-content: space-between; }
  .brand { display: flex; align-items: center; gap: 5px; font-weight: 700; font-size: 11px; letter-spacing: 1px; color: var(--white); }
  .brand-mark { width: 9px; height: 9px; background: var(--blue); }
  .nav { display: flex; align-items: center; gap: 16px; font-size: 6px; font-weight: 600; letter-spacing: .8px; }
  .nav a { color: var(--white); text-decoration: none; }
  .nav .active { background: var(--blue); padding: 3px 8px; }
  .nav .books-link { font-family: "Yellowtail", cursive; font-size: 12px; letter-spacing: 0; font-weight: 400; }
  .hero-title { position: absolute; top: 78px; left: 0; right: 0; }
  .hero-script { font-family: "Yellowtail", cursive; font-size: 50px; line-height: 1; display: block; position: relative; z-index: 2; margin-bottom: -24px; }
  .hero-name { font-size: 50px; font-weight: 800; letter-spacing: 6px; color: var(--blue); line-height: 1; }
  .hero-echo { font-size: 18px; font-weight: 700; letter-spacing: 3px; color: rgba(255,255,255,.12); transform: scaleY(-1); line-height: 1; }
  .hero-tag { position: absolute; top: 184px; left: 0; right: 0; }
  .hero-tag h2 { font-size: 10px; font-weight: 700; line-height: 1.2; }
  .hero-tag p { font-size: 6.5px; margin-top: 3px; opacity: .9; line-height: 1.2; }
  .email-field { margin: 9px auto 0; width: 164px; height: 18px; border: 1px solid rgba(255,255,255,.7); display: flex; align-items: center; justify-content: space-between; padding: 0 8px; font-size: 6px; }
  .email-field .go { color: var(--blue); font-size: 8px; }

  /* About */
  .about { position: relative; height: 170px; background: linear-gradient(90deg, #f4f4f6 0%, #e4e4e8 55%, #bdbdc4 100%); overflow: hidden; }
  .about-photo { position: absolute; right: 0; top: 0; width: 260px; height: 170px; background: linear-gradient(135deg, #c9c9ce 0%, #8f8f97 60%, #6c6c74 100%); opacity: .85; }
  .about-copy { position: absolute; left: 48px; top: 32px; width: 300px; }
  .about-copy h3 { font-size: 12px; font-weight: 700; line-height: 1.3; }
  .about-copy p { font-size: 6.5px; color: var(--muted); line-height: 1.6; margin-top: 10px; width: 290px; }
  .about-copy p strong { color: var(--ink); font-weight: 600; }
  .btn-outline { display: inline-block; margin-top: 14px; border: 1px solid var(--blue); font-size: 6px; font-weight: 700; letter-spacing: 1px; padding: 5px 12px; color: var(--ink); }

  /* Feature cards */
  .features { display: flex; height: 150px; }
  .feature { position: relative; flex: 1; display: flex; flex-direction: column; align-items: center; justify-content: flex-end; padding-bottom: 22px; color: var(--white); text-align: center; }
  .feature-podcast { background: linear-gradient(135deg, #8b948d 0%, #5f6663 60%, #3d4140 100%); }
  .feature-course { background: linear-gradient(180deg, #4b86c4 0%, #6b9cc8 40%, #3f6a5a 75%, #2d4d3e 100%); }
  .feature h4 { font-size: 11px; font-weight: 600; line-height: 1.3; width: 200px; }
  .feature .btn-ghost { margin-top: 10px; border: 1px solid var(--white); font-size: 5.5px; font-weight: 700; letter-spacing: 1px; padding: 5px 20px; }

  /* Section heading */
  .section-head { text-align: center; }
  .script-label { font-family: "Yellowtail", cursive; color: var(--blue); font-size: 16px; line-height: 18px; }
  .section-head h3 { font-size: 11px; font-weight: 600; margin-top: 4px; line-height: 14px; }

  /* Books */
  .books { height: 250px; padding-top: 24px; overflow: hidden; }
  .book-row { display: flex; justify-content: center; gap: 14px; margin-top: 16px; }
  .book { width: 104px; text-align: center; }
  .book-cover { position: relative; height: 110px; background: var(--card); display: flex; align-items: center; justify-content: center; }
  .book-art { width: 62px; height: 82px; background: linear-gradient(180deg, #d5d7dc 0%, #80848d 55%, #3c4049 100%); }
  .shop-now { position: absolute; left: 0; right: 0; bottom: 0; height: 17px; background: var(--blue); color: var(--white); font-size: 5.5px; font-weight: 700; letter-spacing: 1px; display: flex; align-items: center; justify-content: center; gap: 22px; }
  .book-title { font-size: 6.5px; color: var(--ink); margin-top: 8px; line-height: 1.35; }
  .book-price { font-size: 7px; font-weight: 700; color: var(--price); margin-top: 7px; line-height: 1.2; }

  /* Posts */
  .posts-head { height: 50px; padding-top: 6px; }
  .posts { display: grid; grid-template-columns: 1fr 1fr; grid-template-rows: 80px 80px; height: 160px; }
  .post { position: relative; display: flex; flex-direction: column; align-items: center; justify-content: center; color: var(--white); text-align: center; }
  .post-night { grid-row: 1 / 3; background: linear-gradient(180deg, #0f2240 0%, #1d3d68 60%, #2a527f 100%); }
  .post-money { background: linear-gradient(135deg, #b8c0b8 0%, #7d8780 100%); }
  .post-research { background: linear-gradient(135deg, #8e8476 0%, #5f5347 100%); }
  .post p { font-size: 8px; font-weight: 600; line-height: 1.35; width: 200px; margin-top: 6px; }

  /* Connect */
  .connect { height: 170px; text-align: center; padding-top: 20px; }
  .connect h2 { font-size: 18px; font-weight: 500; margin-top: 4px; line-height: 22px; }
  .connect .sub { font-size: 7.5px; font-weight: 500; margin-top: 2px; line-height: 10px; }
  .signup { display: flex; justify-content: center; gap: 6px; margin-top: 11px; }
  .field { width: 144px; height: 18px; border: 1px solid var(--line); font-size: 5.5px; color: var(--muted); text-align: left; padding: 5px 7px; line-height: 1; }
  .submit { width: 76px; height: 18px; background: var(--blue); color: var(--white); font-size: 5.5px; font-weight: 700; letter-spacing: 1px; display: flex; align-items: center; justify-content: center; }
  .socials { display: flex; justify-content: center; gap: 6px; margin-top: 12px; }
  .social-dot { width: 14px; height: 14px; border-radius: 50%; background: #8a8e99; }
  .copyright { font-size: 5.5px; margin-top: 9px; font-weight: 700; letter-spacing: .5px; line-height: 8px; }
  .copyright span { color: var(--blue); }
  .rights { font-size: 5px; color: var(--muted); margin-top: 1px; line-height: 8px; }
</style>
</head>
<body>
<div class="page">

  <header class="hero">
    <div class="hero-photo" role="img" aria-label="Dane with arms outstretched in front of a misty pine forest, in muted purple tones"></div>
    <div class="topbar">
      <div class="brand"><span class="brand-mark"></span>DANE WHITAKER</div>
      <nav class="nav">
        <a class="active" href="#">HOME</a>
        <a href="#">MY STORY</a>
        <a href="#">BLOGS</a>
        <a href="#">CONTACT</a>
        <a class="books-link" href="#">Top 100 Books</a>
      </nav>
    </div>
    <div class="hero-title">
      <span class="hero-script">Dane</span>
      <div class="hero-name">WHITAKER</div>
      <div class="hero-echo">DANE WHITAKER</div>
    </div>
    <div class="hero-tag">
      <h2>Live Life on Your Terms</h2>
      <p>Sign up for the latest videos and free content</p>
      <div class="email-field"><span>name@email.com</span><span class="go">&#9656;</span></div>
    </div>
  </header>

  <section class="about">
    <div class="about-photo" role="img" aria-label="Black and white portrait of Dane smiling in a cap and backpack"></div>
    <div class="about-copy">
      <h3>Entrepreneur, traveler and llama lover. Join Dane and his 20,000+ Community on Videohub</h3>
      <p>Dane Whitaker has been an entrepreneur since he was 12 years old. His journey began by selling on <strong>Realm Quest Auction House</strong>. Dane strategically skipped school &amp; stayed up all night to play video games - not because he was an obsessed pre-teen, ...</p>
      <span class="btn-outline">READ MORE</span>
    </div>
  </section>

  <section class="features">
    <div class="feature feature-podcast" role="img" aria-label="Cheering man in a suit surrounded by falling banknotes">
      <h4>How to Capitalize on a Short-Team Product Trend</h4>
      <span class="btn-ghost">PODCAST</span>
    </div>
    <div class="feature feature-course" role="img" aria-label="Hikers with backpacks celebrating on a mountain summit above a bay">
      <h4>The First Free Shopvane Private Label Course</h4>
      <span class="btn-ghost">SIGN UP NOW</span>
    </div>
  </section>

  <section class="books">
    <div class="section-head">
      <div class="script-label">Top 100 Books</div>
      <h3>Live Life on Your Terms</h3>
    </div>
    <div class="book-row">
      <div class="book">
        <div class="book-cover"><div class="book-art" role="img" aria-label="Book cover with portrait of Dane"></div></div>
        <div class="book-title">Pulse Life Management<br>System (Planner)</div>
        <div class="book-price">£21.50</div>
      </div>
      <div class="book">
        <div class="book-cover"><div class="book-art" role="img" aria-label="Book cover with portrait of Dane"></div><div class="shop-now"><span>SHOP NOW</span><span>&rarr;</span></div></div>
        <div class="book-title">Ultimate Relationship<br>Program</div>
        <div class="book-price">£18.50</div>
      </div>
      <div class="book">
        <div class="book-cover"><div class="book-art" role="img" aria-label="Book cover with portrait of Dane"></div></div>
        <div class="book-title">Your Financial Freedom<br>Playbook</div>
        <div class="book-price">£21.50</div>
      </div>
      <div class="book">
        <div class="book-cover"><div class="book-art" role="img" aria-label="Book cover with portrait of Dane"></div></div>
        <div class="book-title">Pulse Life Management<br>System (Planner)</div>
        <div class="book-price">£21.50</div>
      </div>
      <div class="book">
        <div class="book-cover"><div class="book-art" role="img" aria-label="Book cover with portrait of Dane"></div></div>
        <div class="book-title">Ultimate Relationship<br>Program</div>
        <div class="book-price">£18.50</div>
      </div>
    </div>
  </section>

  <div class="section-head posts-head">
    <div class="script-label">Recent Posts</div>
    <h3>Keep Going. Start Chasing the Passion.</h3>
  </div>

  <section class="posts">
    <article class="post post-night" role="img" aria-label="Telescope silhouette under a starry night sky">
      <svg width="18" height="18" viewBox="0 0 18 18" aria-hidden="true"><circle cx="9" cy="9" r="8" fill="none" stroke="#1a8ae6" stroke-width="1.5"/><path d="M7 5.5v7l5.5-3.5z" fill="#1a8ae6"/></svg>
      <p>Trend Rocket product discovery DESTROYS CANOPY FINDER niche hunter ?</p>
    </article>
    <article class="post post-money" role="img" aria-label="Man at a desk among flying banknotes">
      <svg width="18" height="18" viewBox="0 0 18 18" aria-hidden="true"><circle cx="9" cy="9" r="8" fill="none" stroke="#1a8ae6" stroke-width="1.5"/><path d="M7 5.5v7l5.5-3.5z" fill="#1a8ae6"/></svg>
      <p>How much money do you need to get started on Shopvane?</p>
    </article>
    <article class="post post-research" role="img" aria-label="Tired man resting his head on a table beside coffee cups">
      <svg width="18" height="18" viewBox="0 0 18 18" aria-hidden="true"><circle cx="9" cy="9" r="8" fill="none" stroke="#1a8ae6" stroke-width="1.5"/><path d="M7 5.5v7l5.5-3.5z" fill="#1a8ae6"/></svg>
      <p>Shopvane SVF product research 7 Failed Products in a row!</p>
    </article>
  </section>

  <footer class="connect">
    <div class="script-label">Let's Connect</div>
    <h2>Join 40,000+ Shopvane Sellers.</h2>
    <p class="sub">Sign up for the latest videos &amp; free content.</p>
    <form class="signup">
      <div class="field">Your Name</div>
      <div class="field">Your Email</div>
      <div class="submit">SUBMIT</div>
    </form>
    <div class="socials">
      <span class="social-dot"></span><span class="social-dot"></span><span class="social-dot"></span>
    </div>
    <p class="copyright">© 2018 DANE <span>WHITAKER.</span></p>
    <p class="rights">All Rights Reserved.</p>
  </footer>

</div>
</body>
</html>
```